Book Cover design - Book Series about Animal Assisted Interventions need Book cover design -

Name of First Book - Opening Gates - Your Early Days in Creature Supported Care, by Dr Harriet Pembrook. We are seeking an emotive, symbolic, and cohesive cover design for The Bright Series – a ten-part book collection exploring the therapeutic power of animals in education, care, therapy, and professional growth. The series is written by the founder of Marrowind, a UK-based therapeutic organisation that works with over 30 species to support children, families, and professionals.

The design should reflect the heart-led, reflective, and transformative nature of the series. Core themes include emotional connection, healing, purpose, courage, and growth. Each book will focus on a specific theme or species (e.g. dogs, llamas, leadership, burnout, personal growth) but should visually connect as part of a unified collection.

Key design elements:

(Open to suggestions however currently leaning on - ) not essential - feel free to try other things - probably Deep purple background as the grounding colour

Warm orange for accents (energy, hope) (again open to suggestions - different designs)

possibly Black or white silhouettes for symbolic human–animal imagery.. BUT OPEN ALL DIFFERENT DESIGNS!

Please don't use the actual Logos on the design, but it would be good if there was some theme that resonates them together - like style/colour

Clean, elegant typography (with “BRIGHT” as the visual anchor in every title)

Symbolism encouraged (paths, hearts, trees, circles, rising suns). I like the ones where a human is touching calmly with an animal, either looking at each other, walking together, sitting together etc.. Vulnerable people is often more powerful (like children or older people)

Visual “nod” to the Marrowind brand style – soft curves, emotional tone, nature-inspired calm

Designers are invited to submit a concept for the books with some finished designs. Each cover should stand alone while fitting beautifully into a recognisable series.

Target Market(s)

Teachers, therapists, professionals, adults, mature adults, Mature students

Industry/Entity Type

Therapy, education, animal work, pet therapy

Font styles to use
Sans Serif

Colors

Designer to choose colors to be used in the design.

Requirements
Must have
• Deep emotion, calm, intrigue,
Nice to have
• Deep colours, features of animals and people, Book title, Author name - Harriet Pembrook
Should not have
• Not be childish/for children

```html
<!DOCTYPE html>
<html lang="en">
<head>
<meta charset="utf-8">
<title>Bright With Spirit and Setters – Harriet Pembrook</title>
<link rel="stylesheet" href="https://fonts.googleapis.com/css2?family=Poppins:wght@300;400;600;700;800&family=Great+Vibes&display=swap">
<style>
  :root {
    --page: #ffffff;
    --purple-top: #30035a;
    --purple-mid: #4a0a5c;
    --horizon: #4a0748;
    --purple-low: #24033f;
    --purple-deep: #1c0233;
    --disc: #35065a;
    --orange: #f7923a;
    --white: #ffffff;
    --rule: rgba(255,255,255,0.75);
  }
  * { margin: 0; padding: 0; box-sizing: border-box; }
  html, body {
    width: 930px; height: 1200px; overflow: hidden;
    background: var(--page);
  }
  .cover {
    position: absolute; left: 89px; top: 73px;
    width: 752px; height: 1054px; overflow: hidden;
    font-family: "Poppins", sans-serif; color: var(--white);
    background: linear-gradient(180deg,
      var(--purple-top) 0%,
      var(--purple-top) 22%,
      var(--purple-mid) 45%,
      var(--horizon) 55%,
      var(--purple-low) 70%,
      var(--purple-deep) 100%);
  }
  .dusk-glow {
    position: absolute; left: 0; top: 500px; width: 752px; height: 200px;
    background: linear-gradient(180deg, rgba(120,10,90,0) 0%, rgba(110,10,80,0.35) 55%, rgba(40,3,60,0) 100%);
  }
  .texture {
    position: absolute; background: var(--orange); opacity: 0.12; border-radius: 2px;
  }
  .texture--top { left: 58px; top: 68px; width: 32px; height: 47px; }
  .texture--bottom { left: 662px; top: 812px; width: 32px; height: 48px; }
  .texture--stripes {
    left: 649px; top: 401px; width: 103px; height: 207px;
    background: var(--white); opacity: 0.05;
    border-radius: 100px 0 0 100px;
  }
  .series-word {
    position: absolute; left: 0; width: 100%; top: 64px;
    text-align: center; font-weight: 600; font-size: 106px; line-height: 1;
    letter-spacing: -1px;
  }
  .connector {
    position: absolute; left: 0; width: 100%; top: 166px; height: 70px;
  }
  .connector .rule {
    position: absolute; top: 27px; height: 1px; background: var(--rule);
  }
  .rule--left { left: 150px; width: 154px; }
  .rule--right { left: 451px; width: 154px; }
  .connector .joiner {
    position: absolute; left: 0; width: 100%; top: 0;
    text-align: center; font-family: "Great Vibes", cursive; font-size: 56px; line-height: 1;
  }
  .title {
    position: absolute; left: 0; width: 100%;
    text-align: center; font-size: 95px; line-height: 1; white-space: nowrap;
  }
  .title--first { top: 218px; }
  .title--second { top: 300px; }
  .title .accent { color: var(--orange); font-weight: 700; }
  .title .light { font-weight: 300; }
  .moon {
    position: absolute; left: 213px; top: 445px;
    width: 326px; height: 326px; border-radius: 50%;
    background: var(--disc);
  }
  .silhouette {
    position: absolute; left: 271px; top: 424px; width: 210px; height: 382px;
    border-radius: 40px;
    background: linear-gradient(180deg, rgba(255,255,255,0.85), rgba(255,255,255,0.7));
  }
  .subtitle {
    position: absolute; left: 0; width: 100%;
    text-align: center; font-size: 35px; line-height: 1;
  }
  .subtitle--lead { top: 850px; font-weight: 300; }
  .subtitle--main { top: 889px; font-weight: 600; }
  .byline {
    position: absolute; left: 0; width: 100%; top: 951px;
    text-align: center; font-size: 31px; line-height: 1; white-space: nowrap;
  }
  .byline .by { font-weight: 400; letter-spacing: 0.1em; margin-right: 10px; }
  .byline .author { font-weight: 700; color: var(--orange); letter-spacing: 0.16em; }
</style>
</head>
<body>
  <main class="cover">
    <div class="dusk-glow"></div>
    <div class="texture texture--top" role="img" aria-label="Small grid of orange dots"></div>
    <div class="texture texture--bottom" role="img" aria-label="Small grid of orange dots"></div>
    <div class="texture texture--stripes" role="img" aria-label="Faint diagonal line pattern in a curved shape"></div>

    <h1>
      <span class="series-word">Bright</span>
      <span class="connector">
        <span class="rule rule--left"></span>
        <span class="joiner">With</span>
        <span class="rule rule--right"></span>
      </span>
      <span class="title title--first"><span class="accent">SPIRIT</span> <span class="light">AND</span></span>
      <span class="title title--second"><span class="accent">SETTERS</span></span>
    </h1>

    <div class="moon"></div>
    <div class="silhouette" role="img" aria-label="White silhouette of a small dog standing on the back of a larger dog, both looking upward"></div>

    <p class="subtitle subtitle--lead">The Gentle Strength of</p>
    <p class="subtitle subtitle--main">Dogs in Care and Comfort</p>
    <p class="byline"><span class="by">BY</span><span class="author">HARRIET PEMBROOK</span></p>
  </main>
</body>
</html>
```